Kid's Cancer Camp Business Card

Create a unique Two-Sided color business cards for Camp Willow Brook, a pediatric cancer camp.

The camp tag line is: Where brave young campers laugh and play...

Dale Morrisey, Executive Director
Camp Willow Brook Charitable Foundation, Inc
PO Box 918
Larkfield, CT 06832

Phone - 203-555-0143
Fax - 203-555-0187
Email: dale@campwillowbrook.example
www.campwillowbrook.example

Target Market(s)

Potential Donors, Volunteers and Campers

Industry/Entity Type

Non-profit pediatric cancer camp

Contact Information for Business Card

All contact info that is included in the description

Font styles to use
Other font styles liked:
• Designer chooses font

Requirements
Must have
• Camp Willow Brook Logo and Tag Line
Nice to have
• should be eye catching
Should not have
• not cartoony

```html
<!DOCTYPE html>
<html lang="en">
<head>
<meta charset="utf-8">
<title>Camp Willow Brook – Business Card</title>
<link rel="stylesheet" href="https://fonts.googleapis.com/css2?family=Montserrat:ital,wght@0,400;0,500;0,700;1,400&display=swap">
<style>
  :root {
    --sun: #fbb22a;
    --teal: #00a69a;
    --navy: #0e6aa0;
    --ink: #1f1f1f;
    --paper: #ffffff;
    --backdrop: #ededeb;
  }
  * { box-sizing: border-box; margin: 0; padding: 0; }
  html, body {
    width: 1200px; height: 1200px; overflow: hidden;
    background: var(--backdrop);
    font-family: "Montserrat", Arial, sans-serif;
  }
  .canvas { position: relative; width: 1200px; height: 1200px; }

  .card {
    position: absolute; left: 198px; width: 806px; height: 475px;
    overflow: hidden;
  }
  .card--front { top: 98px; background: var(--paper); }
  .card--back { top: 648px; background: var(--teal); }

  /* front */
  .org-band {
    position: absolute; left: 85px; right: 0; top: 37px; height: 59px;
    background: var(--sun);
    display: flex; align-items: center; justify-content: flex-end;
    padding-right: 50px;
    font-weight: 700; font-size: 20px; letter-spacing: 0.3px;
    color: var(--ink); text-transform: uppercase;
  }
  .brand {
    position: absolute; left: 55px; top: 150px; width: 380px;
    display: flex; flex-direction: column; align-items: center; gap: 16px;
  }
  .brand-dot {
    width: 86px; height: 86px; border-radius: 50%; background: var(--sun);
  }
  .brand-name {
    font-weight: 500; font-size: 28px; line-height: 1.1; color: var(--teal);
  }
  .tagline {
    position: absolute; left: 52px; width: 386px; top: 306px; text-align: center;
    font-style: italic; font-size: 17.5px; line-height: 1.2; color: var(--ink);
  }
  .address-block {
    position: absolute; left: 0; top: 359px; width: 384px; height: 90px;
    background: var(--teal); color: var(--paper);
    display: flex; align-items: center; justify-content: flex-end; gap: 12px;
    padding-right: 44px; font-size: 20px; line-height: 1.45; letter-spacing: 0.4px;
  }
  .address-block address { font-style: normal; text-align: right; }
  .address-block .icon { align-self: flex-start; margin-top: 20px; }

  .person {
    position: absolute; right: 51px; top: 176px; text-align: right;
  }
  .person-name {
    font-weight: 700; font-size: 28px; color: var(--navy); letter-spacing: 0.8px;
  }
  .person-title { margin-top: 8px; font-size: 19px; color: var(--ink); }

  .contacts {
    position: absolute; right: 50px; top: 312px; list-style: none;
    font-size: 19px; color: var(--ink); letter-spacing: 0.3px;
  }
  .contacts li {
    display: flex; justify-content: flex-end; align-items: center; gap: 16px;
    height: 30px;
  }
  .icon { width: 15px; height: 15px; flex: none; }
  .icon--teal { color: var(--teal); }

  /* back */
  .back-brand {
    position: absolute; inset: 0;
    display: flex; flex-direction: column; align-items: center; justify-content: center;
    gap: 30px; padding-top: 20px;
  }
  .back-brand .brand-dot { width: 170px; height: 170px; }
  .back-brand .brand-name { font-size: 48px; color: var(--paper); }
</style>
</head>
<body>
<main class="canvas">

  <section class="card card--front" aria-label="Business card front">
    <div class="org-band">Camp Willow Brook Charitable Foundation, Inc</div>

    <div class="brand">
      <span class="brand-dot" aria-hidden="true"></span>
      <span class="brand-name">Camp Willow Brook</span>
    </div>
    <p class="tagline">Where brave young campers laugh and play...</p>

    <div class="address-block">
      <address>PO Box 918<br>Larkfield, CT 06832</address>
      <svg class="icon" viewBox="0 0 16 16" aria-hidden="true">
        <path d="M8 1a4.5 4.5 0 0 0-4.5 4.5C3.5 9 8 13 8 13s4.5-4 4.5-7.5A4.5 4.5 0 0 0 8 1z" fill="none" stroke="#fff" stroke-width="1.6"/>
        <circle cx="8" cy="5.5" r="1.5" fill="#fff"/>
        <path d="M3 15h10" stroke="#fff" stroke-width="1.6"/>
      </svg>
    </div>

    <div class="person">
      <h1 class="person-name">DALE MORRISEY</h1>
      <p class="person-title">Executive Director</p>
    </div>

    <ul class="contacts">
      <li>203-555-0143
        <svg class="icon icon--teal" viewBox="0 0 16 16" aria-label="Phone">
          <path d="M4 1.5l2.3 2.8-1.3 1.6a8 8 0 0 0 5.1 5.1l1.6-1.3 2.8 2.3-1.5 2.3C7.5 14 2 8.5 1.7 3z" fill="currentColor"/>
        </svg>
      </li>
      <li>203-555-0187
        <svg class="icon icon--teal" viewBox="0 0 16 16" aria-label="Fax">
          <rect x="4" y="1" width="8" height="4" fill="currentColor"/>
          <rect x="1" y="5.5" width="14" height="6" rx="1" fill="currentColor"/>
          <rect x="4" y="9.5" width="8" height="5.5" fill="#fff" stroke="currentColor" stroke-width="1.4"/>
        </svg>
      </li>
      <li>dale@campwillowbrook.example
        <svg class="icon icon--teal" viewBox="0 0 16 16" aria-label="Email">
          <rect x="1" y="3" width="14" height="10" fill="currentColor"/>
          <path d="M1.5 3.5L8 9l6.5-5.5" fill="none" stroke="#fff" stroke-width="1.3"/>
        </svg>
      </li>
      <li>www.campwillowbrook.example
        <svg class="icon icon--teal" viewBox="0 0 16 16" aria-label="Website">
          <circle cx="8" cy="8" r="7" fill="currentColor"/>
          <path d="M1 8h14M8 1c-3 3.5-3 10.5 0 14M8 1c3 3.5 3 10.5 0 14" fill="none" stroke="#fff" stroke-width="1"/>
        </svg>
      </li>
    </ul>
  </section>

  <section class="card card--back" aria-label="Business card back">
    <div class="back-brand">
      <span class="brand-dot" aria-hidden="true"></span>
      <span class="brand-name">Camp Willow Brook</span>
    </div>
  </section>

</main>
</body>
</html>
```